Local Real Estate Office needs an innovative Letterhead Design

Using the attached Logo, please create a letterhead design that is innovative and unusual. I am looking for something that will appeal to young homebuyers as well as seniors going into Condos.

The attached logo for Marrowfield Hearth needs to be included (small but readable) as well as spaces for 2 agents "head shots" photos.
Updates

I need a spot on the letterhead for two photos (head shots). thx

Industry/Entity Type

Real Estate

```html
<!DOCTYPE html>
<html lang="en">
<head>
<meta charset="utf-8">
<title>Marrowfield Hearth Letterhead</title>
<link href="https://fonts.googleapis.com/css2?family=Questrial&display=swap" rel="stylesheet">
<style>
  :root {
    --navy: #1f3566;
    --grey: #8c8f94;
    --text: #5b5e63;
    --paper: #ffffff;
    --backdrop: #e9eaec;
    --photo-a: #c9cdd3;
    --photo-b: #b9bec6;
  }
  * { margin: 0; padding: 0; box-sizing: border-box; }
  html, body {
    width: 1200px; height: 936px; overflow: hidden;
    background: var(--backdrop);
    font-family: "Questrial", "Century Gothic", sans-serif;
  }
  .letterhead {
    position: absolute; left: 255px; top: 22px;
    width: 690px; height: 892px;
    background: var(--paper);
    box-shadow: 0 2px 10px rgba(0,0,0,0.12);
  }
  .brand {
    position: absolute; left: 44px; top: 48px;
    display: flex; align-items: center; gap: 8px;
  }
  .brand-mark { width: 12px; height: 12px; background: var(--grey); }
  .brand-name { font-size: 24px; color: var(--navy); letter-spacing: 0.2px; }
  .footer-rule { position: absolute; left: 0; top: 0; width: 690px; height: 892px; pointer-events: none; }
  .agent-photo {
    position: absolute; top: 740px; width: 66px; height: 66px;
    background: linear-gradient(160deg, var(--photo-a), var(--photo-b));
  }
  .agent-photo.first { left: 60px; }
  .agent-photo.second { left: 136px; }
  .contact {
    position: absolute; left: 216px; top: 776px;
    font-size: 9.5px; line-height: 14px; color: var(--text);
  }
  .contact b { color: var(--navy); font-weight: normal; }
</style>
</head>
<body>
  <main class="letterhead">
    <div class="brand">
      <span class="brand-mark"></span>
      <span class="brand-name">Marrowfield Hearth</span>
    </div>

    <div class="agent-photo first" role="img" aria-label="Head shot of the first agent"></div>
    <div class="agent-photo second" role="img" aria-label="Head shot of the second agent"></div>

    <div class="contact">
      <p>218-42nd Avenue West Larchmoor, Northvale, N4K 2B8</p>
      <p><b>T:</b> (555) 310-4721 · <b>F:</b> (555) 310-4790 · www.marrowfieldhearth.ca</p>
    </div>

    <svg class="footer-rule" viewBox="0 0 690 892" aria-hidden="true">
      <polyline points="0,832 34,832 52,814 600,814 618,792 690,792"
                fill="none" stroke="var(--navy)" stroke-width="3.5"/>
    </svg>
  </main>
</body>
</html>
```